Business Card Update, need to bring life to the card, two sided color

We need a new business card design, are moving and changing addresses and need a new look, we have the logos already attached but need a new style moving forward. Can incorporate the color of the logo (The Green) as well, maybe a solid back? We deal with safety products revolving around static electricity and safety lighting. Would like to keep same font in second logo as well.

Target Market(s)

Electrical Safety, Lighting

Contact Information for Business Card

Lars Whitcombe
Vice President
Office: 555-284-7316
Cell: 555-862-0457
lars@tkwhitcombe.com
www.tkwhitcombe.com
4700 West Cedar Boulevard
Suite #320
Roswell, GA 30412

Font styles to use
Serif
Sans Serif

Requirements
Must have
• Since 1918
Nice to have
• Could use the 100 Year Logo for back of card, would like the back of card to be the same green as logo.
Should not have
• No black cards please.

```html
<!DOCTYPE html>
<html lang="en">
<head>
<meta charset="utf-8">
<title>T.K. Whitcombe – Business Card</title>
<link rel="stylesheet" href="https://fonts.googleapis.com/css2?family=Montserrat:wght@600;700;800&family=Arimo:wght@400;700&display=swap">
<style>
  :root {
    --brand-green: #0f9a5a;
    --deep-green: #0b7a47;
    --card-light: #f4f6f5;
    --ink: #2a2d2e;
    --muted-ink: #4a4f50;
    --stage: #2b2c2f;
    --white: #ffffff;
  }
  * { margin: 0; padding: 0; box-sizing: border-box; }
  html, body { width: 1200px; height: 800px; overflow: hidden; }
  body {
    background: var(--stage);
    font-family: "Arimo", Arial, sans-serif;
    display: flex;
    align-items: center;
    justify-content: center;
    gap: 40px;
  }
  .card {
    position: relative;
    width: 540px;
    height: 310px;
    overflow: hidden;
    box-shadow: 0 18px 40px rgba(0,0,0,.45);
  }

  /* Green side */
  .card--front { background: var(--brand-green); }
  .front-mark {
    position: absolute;
    left: 50%; top: 62px;
    transform: translateX(-50%);
    width: 130px; height: 130px;
    border-radius: 50%;
    background: var(--white);
    display: flex; align-items: center; justify-content: center;
    text-align: center;
  }
  .mark-name {
    font-family: "Montserrat", Arial, sans-serif;
    font-weight: 800;
    color: var(--brand-green);
    letter-spacing: .5px;
    line-height: 1.15;
  }
  .front-mark .mark-name { font-size: 15px; }
  .front-web {
    position: absolute;
    left: 0; right: 0; top: 212px;
    text-align: center;
    font-family: "Montserrat", Arial, sans-serif;
    font-weight: 700;
    font-size: 15px;
    color: var(--white);
    letter-spacing: .3px;
  }
  .front-since {
    position: absolute;
    left: 0; right: 0; top: 240px;
    text-align: center;
    font-family: "Montserrat", Arial, sans-serif;
    font-weight: 600;
    font-size: 12px;
    color: var(--white);
    letter-spacing: 2px;
    text-transform: uppercase;
  }

  /* Light side */
  .card--back { background: var(--card-light); }
  .back-mark {
    position: absolute;
    left: 34px; top: 46px;
    width: 112px; height: 112px;
    border-radius: 50%;
    background: var(--brand-green);
    display: flex; align-items: center; justify-content: center;
    text-align: center;
    z-index: 2;
  }
  .back-mark .mark-name { font-size: 12px; color: var(--white); }
  .company {
    position: absolute;
    left: 164px; top: 40px;
    font-family: "Montserrat", Arial, sans-serif;
  }
  .company__name {
    font-weight: 800;
    font-size: 30px;
    color: var(--brand-green);
    line-height: 1;
  }
  .company__tagline {
    font-weight: 700;
    font-size: 14px;
    color: var(--ink);
    margin-top: 4px;
  }
  .company__since {
    font-weight: 600;
    font-size: 11px;
    color: var(--deep-green);
    letter-spacing: 2px;
    text-transform: uppercase;
    margin-top: 4px;
  }
  .name-band {
    position: absolute;
    left: 0; right: 0; top: 150px;
    height: 38px;
    background: var(--brand-green);
    display: flex; align-items: baseline;
    padding: 8px 0 0 164px;
    gap: 10px;
    font-family: "Montserrat", Arial, sans-serif;
    color: var(--white);
  }
  .name-band__person { font-weight: 700; font-size: 19px; }
  .name-band__title { font-weight: 600; font-size: 12px; letter-spacing: .5px; }
  .contact-list {
    position: absolute;
    right: 272px; top: 200px;
    list-style: none;
    font-size: 13px;
    color: var(--ink);
    line-height: 19px;
  }
  .contact-list li {
    display: flex; align-items: center; justify-content: flex-end; gap: 8px;
  }
  .contact-list .label { color: var(--deep-green); font-weight: 700; }
  .contact-list svg { width: 13px; height: 13px; flex: none; }
  .contact-list .accent { color: var(--brand-green); }
  .divider {
    position: absolute;
    left: 280px; top: 200px;
    width: 2px; height: 76px;
    background: var(--brand-green);
  }
  .address {
    position: absolute;
    left: 296px; top: 200px;
    font-size: 13px;
    color: var(--ink);
    line-height: 19px;
  }
  .base-stripe {
    position: absolute;
    left: 0; right: 0; bottom: 6px;
    height: 5px;
    background: var(--brand-green);
  }
</style>
</head>
<body>

  <section class="card card--front" aria-label="Card front">
    <div class="front-mark"><span class="mark-name">T.K.<br>WHITCOMBE</span></div>
    <p class="front-web">www.tkwhitcombe.com</p>
    <p class="front-since">Since 1918</p>
  </section>

  <section class="card card--back" aria-label="Card back">
    <div class="back-mark"><span class="mark-name">T.K.<br>WHITCOMBE</span></div>
    <div class="company">
      <p class="company__name">T.K. Whitcombe</p>
      <p class="company__tagline">Manufacturing Company, Inc.</p>
      <p class="company__since">Since 1918</p>
    </div>

    <div class="name-band">
      <p class="name-band__person">Lars Whitcombe</p>
      <p class="name-band__title">Vice President</p>
    </div>

    <ul class="contact-list">
      <li><span><span class="label">Office</span> 555-284-7316</span>
        <svg viewBox="0 0 16 16" aria-hidden="true"><path fill="#0f9a5a" d="M3.6 1.5l2.3 2.6-1.3 1.8c.9 2 2.5 3.6 4.5 4.5l1.8-1.3 2.6 2.3-1.4 2.4C6.6 13.6 2.4 9.4 1.2 3z"/></svg>
      </li>
      <li><span><span class="label">Cell</span> 555-862-0457</span>
        <svg viewBox="0 0 16 16" aria-hidden="true"><rect x="4" y="1" width="8" height="14" rx="1.5" fill="#0f9a5a"/><rect x="5.5" y="3" width="5" height="8" fill="#f4f6f5"/></svg>
      </li>
      <li>lars@tkwhitcombe.com
        <svg viewBox="0 0 16 16" aria-hidden="true"><rect x="1" y="3" width="14" height="10" fill="#0f9a5a"/><path d="M1.5 3.5L8 9l6.5-5.5" fill="none" stroke="#f4f6f5" stroke-width="1.4"/></svg>
      </li>
      <li><span>www.<span class="accent">tkwhitcombe</span>.com</span>
        <svg viewBox="0 0 16 16" aria-hidden="true"><circle cx="8" cy="8" r="6.5" fill="none" stroke="#0f9a5a" stroke-width="1.6"/><ellipse cx="8" cy="8" rx="2.8" ry="6.5" fill="none" stroke="#0f9a5a" stroke-width="1.2"/><path d="M1.5 8h13" stroke="#0f9a5a" stroke-width="1.2"/></svg>
      </li>
    </ul>

    <div class="divider"></div>

    <p class="address">4700 West Cedar Boulevard<br>Suite #320<br>Roswell, GA 30412</p>

    <div class="base-stripe"></div>
  </section>

</body>
</html>
```